Australian Skilled Migration

We need to design a add/flyer for a newspaper/magazine to promote our Australian Migration firm services. We targeting overseas graduating students and professionals who would like to Permanently Migrate to Australia.

We would like to advertise following services to our potential clients:

AUSTRALIA NEEDS YOU!!!

# Are you young and energetic individual?
# Do you have qualifications, work experiences or both?
# Perhaps you would like to open a small business, and sponsor yourself to live in Australia?
# Aspiring for job security and the highest living standards?

Contact us to find out how we can help you with Permanent Migration to Australia.

First consultation and eligibility assessment is free ! Tell your friends about us and receive a discount on your future fees!!

For more information please visit our website: www.pelmora-links.org.au

(for a background we would like to use Australian themes such as: sandy beaches, ect... light colours)

Target Market(s)

Students
University graduates
Trade people with qualifications
Industry professionals
Anyone who wants to migrate to Australia

Industry/Entity Type

Security

Requirements
Must have
• our logo and website
easy to see and read the txt

Catchy Background
Nice to have
• as per our requirements
(designer questions, please e-mail: info@pelmora-links.org. au)

```html
<!DOCTYPE html>
<html lang="en">
<head>
<meta charset="utf-8">
<title>Australia Needs You – Pelmora Links</title>
<link href="https://fonts.googleapis.com/css2?family=Montserrat:wght@700&family=Open+Sans:wght@400;600;700&display=swap" rel="stylesheet">
<style>
  :root {
    --sky: #8fc6ea;
    --harbour: #2f7fb6;
    --navy: #1f2370;
    --navy-light: #34399a;
    --red: #e41e26;
    --white: #ffffff;
    --panel: #f1f1f3;
    --ink: #4a4a4f;
  }
  * { margin: 0; padding: 0; box-sizing: border-box; }
  html, body { width: 849px; height: 1200px; overflow: hidden; background: var(--white); }
  .flyer {
    position: relative; width: 849px; height: 1200px; overflow: hidden;
    font-family: "Open Sans", Arial, sans-serif;
  }
  .backdrop { position: absolute; inset: 0; }
  .headline {
    position: absolute; left: 64px; top: 39px; width: 725px; height: 241px;
    background: var(--red); border: 5px solid var(--white);
    outline: 3px solid var(--red);
    box-shadow: 4px 6px 10px rgba(0,0,0,.3);
    display: flex; flex-direction: column; justify-content: center; align-items: center;
    color: var(--white); font-family: "Montserrat", Arial, sans-serif; font-weight: 700;
    font-size: 94px; line-height: 100px; letter-spacing: 0; white-space: nowrap;
  }
  .headline span { display: block; }
  .questions {
    position: absolute; left: 46px; top: 572px; width: 740px; list-style: none;
  }
  .questions li {
    position: relative; padding-left: 40px; color: var(--white);
    font-size: 24px; font-weight: 600; line-height: 29px; margin-bottom: 29px;
  }
  .questions li svg { position: absolute; left: 0; top: 0; width: 32px; height: 32px; }
  .contact {
    position: absolute; left: 33px; top: 915px; width: 720px; height: 285px;
    background: var(--panel);
  }
  .contact-tab {
    position: absolute; left: 0; top: 0; width: 315px; height: 60px;
    background: var(--red); color: var(--white);
    clip-path: polygon(0 0, 100% 0, 87% 100%, 0 100%);
    font-size: 34px; font-weight: 600; line-height: 60px; padding-left: 22px;
    white-space: nowrap;
  }
  .contact-text {
    position: absolute; left: 22px; top: 72px; width: 640px;
    color: var(--ink); font-size: 16.5px; line-height: 23px; white-space: nowrap;
  }
  .contact-more { position: absolute; left: 22px; top: 165px; color: var(--ink); font-size: 16.5px; white-space: nowrap; }
  .contact-web { position: absolute; left: 22px; top: 190px; color: var(--ink); font-size: 28px; font-weight: 700; white-space: nowrap; }
  .brand {
    position: absolute; left: 418px; top: 168px; display: flex; align-items: center; gap: 7px;
    color: var(--red); font-weight: 700; white-space: nowrap;
  }
  .brand-dot { width: 44px; height: 44px; border-radius: 50%; border: 2px solid var(--red); flex: none; }
  .brand-name { display: block; font-size: 18px; line-height: 21px; }
  .brand-tag { display: block; font-size: 10px; line-height: 13px; }
  .agent {
    position: absolute; right: 0; top: 870px; width: 170px; height: 330px;
    background: linear-gradient(180deg, #8a5a3c 0%, #c99b7c 40%, #f4f4f6 75%, #ffffff 100%);
    border-top-left-radius: 90px;
  }
</style>
</head>
<body>
<div class="flyer">
  <svg class="backdrop" width="849" height="1200" viewBox="0 0 849 1200">
    <defs>
      <linearGradient id="harbourView" x1="0" y1="0" x2="0" y2="1">
        <stop offset="0" stop-color="#79b9e6"/>
        <stop offset="0.45" stop-color="#a9d3ee"/>
        <stop offset="0.6" stop-color="#7e8d86"/>
        <stop offset="0.8" stop-color="#2d78ae"/>
        <stop offset="1" stop-color="#1f5f96"/>
      </linearGradient>
      <radialGradient id="navyGlow" cx="0.4" cy="0.45" r="0.7">
        <stop offset="0" stop-color="#3a3fa3"/>
        <stop offset="1" stop-color="#1d2068"/>
      </radialGradient>
    </defs>
    <rect width="849" height="620" fill="url(#harbourView)" role="img" aria-label="Photo of Sydney harbour skyline with the Opera House"/>
    <path d="M0,468 C260,500 560,498 849,585 L849,1200 L0,1200 Z" fill="var(--white)"/>
    <path d="M0,502 C300,520 560,545 849,690 L849,1200 L0,1200 Z" fill="url(#navyGlow)"/>
    <g fill="var(--navy)">
      <polygon points="720,500 730,545 775,540 738,565 760,605 725,580 695,612 705,570 668,550 712,548"/>
      <polygon points="543,558 550,580 572,578 555,592 565,612 545,600 528,615 535,593 517,582 538,580"/>
      <polygon points="632,577 640,603 667,601 645,616 657,640 633,626 612,645 620,618 598,605 624,603"/>
    </g>
    <g fill="var(--white)">
      <polygon points="758,615 766,645 797,642 772,660 788,688 762,672 740,695 746,664 720,650 750,646"/>
      <polygon points="615,657 621,673 639,671 626,682 634,699 617,690 603,703 608,686 593,676 611,674"/>
      <polygon points="750,724 757,741 777,740 762,752 770,772 752,762 735,777 741,757 724,746 744,744"/>
    </g>
  </svg>

  <div class="headline"><span>AUSTRALIA</span><span>NEEDS YOU!!!</span></div>

  <ul class="questions">
    <li><svg viewBox="0 0 34 34"><polygon fill="#c8242e" points="17,1 20,11 30,6 24,15 33,20 22,20 23,31 17,23 11,31 12,20 1,20 10,15 4,6 14,11"/></svg>Are you young and<br>energetic individual?</li>
    <li><svg viewBox="0 0 34 34"><polygon fill="#c8242e" points="17,1 20,11 30,6 24,15 33,20 22,20 23,31 17,23 11,31 12,20 1,20 10,15 4,6 14,11"/></svg>Do you have qualifications, work<br>experiences or both?</li>
    <li><svg viewBox="0 0 34 34"><polygon fill="#c8242e" points="17,1 20,11 30,6 24,15 33,20 22,20 23,31 17,23 11,31 12,20 1,20 10,15 4,6 14,11"/></svg>Perhaps you would like to open a small business, and<br>sponsor yourself to live in Australia?</li>
    <li><svg viewBox="0 0 34 34"><polygon fill="#c8242e" points="17,1 20,11 30,6 24,15 33,20 22,20 23,31 17,23 11,31 12,20 1,20 10,15 4,6 14,11"/></svg>Aspiring for job security and the highest living standards?</li>
  </ul>

  <section class="contact">
    <div class="contact-tab">CONTACT US</div>
    <p class="contact-text">To find out how we can help you with Permanent Migration to Australia.<br>First consultation and eligibility assessment is free !<br>Tell your friends about us and receive a discount on your future fees!!</p>
    <p class="contact-more">For more information please visit our website:</p>
    <p class="contact-web">www.pelmora-links.org.au</p>
    <div class="brand"><span class="brand-dot"></span><span><span class="brand-name">Pelmora Links</span><span class="brand-tag">Lawyers &amp; Migration Agents</span></span></div>
  </section>

  <div class="agent" role="img" aria-label="Photo of a smiling customer service agent wearing a headset"></div>
</div>
</body>
</html>
```